Brise De Lavande is a restaurant and we would like to redesign our old menu.,

Our restaurant menu, ideal for brunch or lunch, showcases French bakery and cafe delights, including quiches, soups, and grown-up grilled cheese. Join us for a culinary journey through France without leaving Marietta, where every bite reflects our passion for quality, tradition, and the joy of French cuisine. Your taste buds will delight in every bite! this Menu Size is 11x 17 tri fold

Target Market(s)

Older Guest 35 to 65

Industry/Entity Type

Food Restaurant

Font styles to use
Serif
Decorative

Colors
0054AA
0677BA
7BADD7
CADEEF
E8F1F8
EB3D1F
EC4F4E
F09395
F8D3D4
FCEDEE

Requirements
Must have
• Larger print to be easier to read but not too large. , 11 x 17 trifold
Nice to have
• I want this menu to be blue as a background and either red as the complementary color or gold

```html
<!DOCTYPE html>
<html lang="en">
<head>
<meta charset="utf-8">
<title>Brise De Lavande – Brunch &amp; Lunch Menu</title>
<link rel="stylesheet" href="https://fonts.googleapis.com/css2?family=Itim&family=Kaushan+Script&family=Lobster&family=Open+Sans:ital,wght@0,700;1,700&display=swap">
<style>
:root{
  --stage:#404042;
  --paper:#e6e6e9;
  --gutter:#f3f3f4;
  --ink-dark:#2a2526;
  --blue:#0054AA;
  --blue-mid:#0677BA;
  --red:#EB3D1F;
  --red-soft:#EC4F4E;
  --heading:#2b2b2b;
}
*{margin:0;padding:0;box-sizing:border-box}
html,body{width:1200px;height:525px;overflow:hidden;background:var(--stage)}
body{position:relative;font-family:"Itim",sans-serif;font-size:5.9px;line-height:6.6px;color:var(--red)}
.spread{position:absolute;top:101px;width:501px;height:324px;background:var(--gutter)}
.spread-outside{left:71px}
.spread-inside{left:628px}
.panel{position:absolute;top:0;width:165px;height:324px;background:var(--paper);overflow:hidden}
.panel-1{left:0}.panel-2{left:168px}.panel-3{left:336px}
.panel-texture{position:absolute;inset:0;background:var(--paper)}
.blk{position:absolute;left:9px;white-space:nowrap}
.n{color:var(--blue);display:block}
.d{color:var(--red);display:block}
.p{position:absolute;right:12px;color:var(--blue);text-align:right;white-space:nowrap}
.box{position:absolute;left:4px;right:4px;border:0.6px dashed var(--red-soft)}
.sec{position:absolute;left:9px;font-family:"Open Sans",sans-serif;font-style:italic;font-weight:700;font-size:8.6px;line-height:10px;color:var(--heading)}
.lbl{color:var(--blue)}
.cover-shape{position:absolute;left:0;top:0}
.brand{position:absolute;top:20px;left:0;right:0;text-align:center;font-size:3.6px;line-height:4px;letter-spacing:1px;text-transform:uppercase;color:var(--red)}
.brand::before{content:"";display:block;width:5px;height:5px;margin:0 auto 2px;background:var(--red)}
.menu-word{position:absolute;top:36px;left:10px;right:10px;display:flex;align-items:center;gap:6px;font-family:"Kaushan Script",cursive;font-size:12px;line-height:14px;color:var(--red)}
.menu-word::before,.menu-word::after{content:"";flex:1;height:0.8px;background:var(--red)}
.title{position:absolute;top:46px;left:0;right:0;text-align:center;font-family:"Kaushan Script",cursive;font-size:33px;line-height:38px;color:var(--red)}
.rule{position:absolute;top:86px;left:10px;right:10px;height:0.8px;background:var(--red)}
.subtitle{position:absolute;top:89px;left:0;right:0;text-align:center;font-family:"Open Sans",sans-serif;font-weight:700;font-size:10.5px;line-height:12px;color:var(--red)}
.tagline{position:absolute;top:102px;left:0;right:0;text-align:center;font-size:5.8px;color:var(--red)}
.breakfast{position:absolute;top:146px;left:8px;font-family:"Lobster",cursive;font-size:14.5px;line-height:17px;color:var(--blue)}
.panel-dark{background:var(--ink-dark);border-radius:0 0 16px 16px}
.cat{color:var(--blue-mid);display:block}
.tiny{font-size:3.6px;line-height:4.2px;color:var(--red-soft)}
.kids{position:absolute;top:51px;left:9px;font-family:"Lobster",cursive;font-size:10px;line-height:12px;color:var(--blue-mid)}
.kids-price{position:absolute;top:70px;right:18px;font-family:"Open Sans",sans-serif;font-weight:700;font-size:22px;line-height:24px;color:var(--red)}
.wine{position:absolute;left:8px;white-space:nowrap;color:var(--red)}
.gl{position:absolute;right:30px;text-align:center}
.bt{position:absolute;right:12px;text-align:center}
.ind{padding-left:10px}
</style>
</head>
<body>

<section class="spread spread-outside" aria-label="Menu outside">
  <div class="panel panel-1">
    <div class="panel-texture" role="img" aria-label="Faint line pattern of pastries and leaves"></div>
    <div class="blk" style="top:6.5px"><span class="n">Eggs Croissant</span><span class="d">two scrambled eggs with Swiss cheese<br>served in a croissant. ham $1.50 chicken<br>Sausage $2.00 bacon $1.50 &nbsp;spinach $.85<br>tomato $.85</span></div>
    <span class="p" style="top:17.2px">$8</span>
    <div class="blk" style="top:42.8px"><span class="n">Fried Egg BLT</span><span class="d">soft fried egg, bacon, lettuce, tomato,<br>avocado, toasted croissant</span></div>
    <span class="p" style="top:50.8px">$11</span>
    <div class="box" style="top:65.5px;height:49.5px"></div>
    <div class="blk" style="top:67.1px"><span class="n">Monte Cristo</span><span class="d">french toast, ham, swiss, bechamel,<br>raspberry jam, fried easy egg +$1.00</span></div>
    <span class="p" style="top:87.1px">$12</span>
    <div class="blk" style="top:93.6px"><span class="n">Parmesan Polenta Bowl</span><span class="d">creamy polenta, parmesan, with chicken<br>sausage, shallots, roasted red peppers</span></div>
    <div class="blk" style="top:117.4px"><span class="n">Quiches</span></div>
    <div class="blk" style="top:124.2px"><span class="lbl">Lorraine:</span> ham, bacon &amp; swiss cheese</div>
    <div class="blk" style="top:132.8px"><span class="lbl">spinach:</span> spinach &amp; swiss cheese</div>
    <span class="p" style="top:124.2px">$10</span>
    <span class="p" style="top:132.8px">$8</span>
    <div class="blk" style="top:144.9px"><span class="n">Yogurt &amp; Granola Parfait</span><span class="d">vanilla greek yogurt, local honey, seasonal<br>fruit, house made almond granola</span></div>
    <span class="p" style="top:150.5px">$8</span>
    <div class="blk" style="top:170.5px"><span class="n">The Grande Breakfast</span><span class="d">Two eggs any style, bacon or chicken<br>sausage, croissant or baguette, choice of<br>hashbrowns, roasted potatoes, fruit</span></div>
    <span class="p" style="top:184.5px">$15</span>
    <div class="blk" style="top:201.7px"><span class="n">Avocado Tartine</span><span class="d">avocado, pickled red onion, dijonaise, chili<br>raisins, alfalfa sprouts, multigrain, flaky<br>salt</span></div>
    <span class="p" style="top:212px">$11</span>
    <div class="blk" style="top:232px"><span class="n">Smoked Salmon Tartine</span><span class="d">truffled scrambled eggs, smoked salmon,<br>pickled red onion, caper berries, cucumber,<br>tomato, arugula, multigrain, herbed cream<br>cheese</span></div>
    <span class="p" style="top:246px">$14</span>
    <div class="blk" style="top:268.8px"><span class="n">Crepe Du Jour</span></div>
    <span class="p" style="top:268.8px">$9</span>
    <div class="box" style="top:276.5px;height:36px"></div>
    <div class="blk" style="top:277.7px"><span class="lbl">sweet:</span> classic crepe, strawberry, banana,<br>chocolate ganache or hazelnut spread<br><span class="lbl">savory:</span> buckwheat crepe, cheddar, bacon,<br>fried egg &nbsp;savory: ham &amp; swiss stuffed<br>crepe, fried easy egg</div>
    <span class="p" style="top:286.5px">$10</span>
  </div>

  <div class="panel panel-2">
    <div class="panel-texture" role="img" aria-label="Faint line pattern of pastries and leaves"></div>
    <svg class="cover-shape" width="165" height="140" viewBox="0 0 165 140" aria-hidden="true"><path d="M0 0H165V108Q82.5 152 0 108Z" fill="#2a2526"/></svg>
    <div class="brand">Brise De Lavande</div>
    <div class="menu-word">Menu</div>
    <div class="title">Restaurant</div>
    <div class="rule"></div>
    <div class="subtitle">BRUNCH &amp; LUNCH</div>
    <div class="tagline">French bakery and cafe</div>
    <div class="breakfast">Breakfast</div>
    <div class="blk" style="top:165.4px"><span class="n">Le Benedicts</span><span class="d">two poached eggs, lemon herb hollandaise, &nbsp;English muffin</span></div>
    <div class="blk" style="top:183.1px"><span class="lbl">classic:</span> canadian bacon</div>
    <div class="blk" style="top:192px"><span class="lbl">salmon:</span> smoked salmon &amp; tomato</div>
    <span class="p" style="top:183.1px;right:16px">$11</span>
    <span class="p" style="top:192px;right:16px">$14</span>
    <div class="blk" style="top:205.5px"><span class="n">Blt &amp; Avocado Omelette</span><span class="d">bacon, arugula, tomato, avocado, cheddar,<br>lemon herb hollandaise</span></div>
    <span class="p" style="top:209.2px;right:16px">$12</span>
    <div class="blk" style="top:233.4px"><span class="n">Pesto Omelette</span><span class="d">roasted red peppers, caramelized onions,<br>chevre, pesto</span></div>
    <span class="p" style="top:240px;right:16px">$13</span>
    <div class="blk" style="top:265.6px"><span class="n">Build Your Own Three Egg Omelette</span><span class="d">Egg white only +$.80 brie $1.35 goat cheese<br>$1.35 swiss $1.35 cheddar $1.35 ham $1.50<br>chicken sausage $3.00 bacon $2.50 spinach<br>$.85 tomatoes $.85 mushrooms $.85 green<br>onions $.85 red peppers $.85</span></div>
    <span class="p" style="top:281px;right:9px">$5.95</span>
  </div>

  <div class="panel panel-3">
    <div class="panel-texture" role="img" aria-label="Faint line pattern of pastries and leaves"></div>
    <div class="blk" style="top:6.5px"><span class="n">Crème Brulee French Toast</span><span class="d">crème brulee soaked brioche, blueberry<br>compote, crème anglaise</span></div>
    <span class="p" style="top:13.5px">$11</span>
    <div class="blk" style="top:31.6px"><span class="n">Belgium Waffle</span><span class="d">speculoos butter, roasted pecan maple syrup</span></div>
    <span class="p" style="top:36.3px">$10</span>
    <div class="sec" style="top:48px">Soups and Salads</div>
    <div class="box" style="top:62px;height:37px"></div>
    <div class="blk" style="top:62.4px"><span class="n">Tomato Basil Soup</span><span class="d">tomato, basil, cream, croutons</span></div>
    <div class="blk" style="top:78.3px"><span class="n">Soup Du Jour</span><span class="d">ask your server for our soup of the<br>day with our homemade croutons</span></div>
    <span class="p" style="top:71.7px">Cup $4</span>
    <span class="p" style="top:80.1px">Bowl $8</span>
    <div class="box" style="top:102.5px;height:50px"></div>
    <div class="blk" style="top:103.9px"><span class="n">Garden Salad</span><span class="d">baby lettuces, english cucumbers, cherry<br>tomato, marinated feta, french<br>vinaigrette</span></div>
    <div class="blk" style="top:130.9px"><span class="n">Caesar Salad</span><span class="d">romaine, parmesan, brioche croutons,<br>lemon parmesan dressing</span></div>
    <span class="p" style="top:120.2px">Small $5</span>
    <span class="p" style="top:128.6px">large $10</span>
    <div class="box" style="top:156px;height:60px"></div>
    <div class="blk" style="top:157px"><span class="n">Marinated Beet Salad</span><span class="d">smoked blue cheese crumbles, balsamic<br>&amp; candied pecans</span></div>
    <div class="blk" style="top:184.5px"><span class="n">Salmon Atlantique</span><span class="d">mixed greens, smoked salmon, golden<br>raisins, walnuts, goat cheese with<br>balsamic dressing</span></div>
    <span class="p" style="top:177.5px">$14</span>
    <div class="sec" style="top:217px">Sandwiches</div>
    <div class="box" style="top:227.5px;height:24px"></div>
    <div class="blk" style="top:228.8px"><span class="n">Jambon Beurre Fromage Baguette</span><span class="d">black forest ham, swiss cheese, butter,<br>baguette.</span></div>
    <span class="p" style="top:229.2px">Half $6</span>
    <span class="p" style="top:237.6px">Whole $10</span>
    <div class="blk" style="top:255.3px"><span class="n">Chicken Salad</span><span class="d">lemon tarragon roast chicken, apples, bibb<br>lettuce, on your choice of butter croissant or<br>baguette</span></div>
    <span class="p" style="top:267px">$10</span>
    <div class="box" style="top:284px;height:37px"></div>
    <div class="blk" style="top:294.4px"><span class="n">Frenchie</span><span class="d">brie, lettuce, tomato, butter, baguette</span></div>
    <span class="p" style="top:295.8px">Half $6</span>
    <span class="p" style="top:304.3px">Whole $10</span>
  </div>
</section>

<section class="spread spread-inside" aria-label="Menu inside">
  <div class="panel panel-1">
    <div class="panel-texture" role="img" aria-label="Faint line pattern of pastries and leaves"></div>
    <div class="box" style="top:4px;height:25px"></div>
    <div class="blk" style="top:6.5px"><span class="n">Les Croques</span><span class="d">black forest ham, swiss cheese, bechamel,<br>pain de mie bread.</span></div>
    <span class="p" style="top:11.5px;right:8px">Smr $5</span>
    <span class="p" style="top:20.8px;right:8px">Mdme $10</span>
    <div class="blk" style="top:33.5px"><span class="n">Grown Up Grilled Cheese</span><span class="d">shaved roast beef, pimento cheese,<br>caramelized onion, horseradish crème,<br>brioche, served with house made pickles</span></div>
    <span class="p" style="top:45.2px">$14</span>
    <div class="blk" style="top:67.1px"><span class="n">Chicken Panini</span><span class="d">marinated chicken, brie, tomato, red onion<br>marmalade, balsamic glaze, ciabatta.</span></div>
    <span class="p" style="top:73.6px">$12</span>
    <div class="blk" style="top:92.7px"><span class="n">L'Italiano</span><span class="d">fresh mozzarella, tomatoes, basil pesto,<br>arugula, balsamic, ciabatta</span></div>
    <span class="p" style="top:99.2px">$10</span>
    <div class="sec" style="top:122px;font-size:9.4px;font-style:normal;color:#1f1f1f">Sides</div>
    <div class="blk" style="top:141.2px;left:16px"><span class="d">fruit salad | roasted potatoes | hash brown<br>bacon | chicken sausage | andouille<br>sausage</span></div>
    <span class="p" style="top:141.2px">$3</span>
    <span class="p" style="top:147.7px">$5</span>
    <div class="blk" style="top:167.7px;left:16px"><span class="d">haricot vert with shallot fresh corn &amp;<br>andouille sausage</span></div>
    <span class="p" style="top:167.7px">$7</span>
    <div class="blk" style="top:185px;left:16px"><span class="d">roasted brussel sprouts, dried cranberries,<br>balsamic</span></div>
    <span class="p" style="top:185px">$6</span>
    <div class="sec" style="top:209px;font-size:9.4px;color:#1f1f1f">Entrees</div>
    <div class="blk" style="top:223.6px"><span class="n">Tourte au Poulet</span><span class="d">marinated chicken, swiss cheese, onion,<br>mushroom, bechamel, flaky pastry</span></div>
    <span class="p" style="top:222.2px">$15</span>
    <div class="blk" style="top:252px"><span class="n">Beef Bourguignon</span><span class="d">red wine braised beef, pearl onions, carrots,<br>mushrooms, buttered egg noodles</span></div>
    <span class="p" style="top:252px">$18</span>
    <div class="blk" style="top:281px"><span class="n">Fork &amp; Knife “French Dip” Tartine</span><span class="d">shaved roast beef, arugula, smoked blue<br>cheese, horseradish crème, pickled onions &amp;<br>au jus</span></div>
    <span class="p" style="top:281px">$16</span>
  </div>

  <div class="panel panel-2 panel-dark">
    <div class="blk" style="top:6.5px"><span class="cat">Ratatouille &amp; eggs</span><span class="d">roasted squash, peppers, eggplant,<br>tomatoes, fresh herbs, choice of two eggs &amp;<br>a side of baguette<br>add bacon, chicken sausage, or andouille<br>sausage</span></div>
    <span class="p" style="top:6.5px;right:7px;color:var(--red)">$14</span>
    <span class="p" style="top:26.5px;right:7px;color:var(--red)">+$5</span>
    <div class="box" style="top:50px;height:63px"></div>
    <div class="kids">Kids Menu</div>
    <div class="blk" style="top:64.3px"><span class="d">French toast with maple syrup<br>Scrambled eggs &amp; bacon platter<br>Egg &amp; cheese breakfast sandwich<br>Strawberry &amp; hazelnut crepe<br>Yogurt and berries<br>Grilled cheese sandwich</span><span class="cat">*All meals served with fruit or potatoes</span></div>
    <div class="kids-price">$7</div>

    <div class="box" style="top:117px;height:21px"></div>
    <div class="wine" style="top:116.5px"><span class="cat">REDS</span>Chateau Valmoreau Cabernet Sauvignon<br>La Petite Ombre Pinot Noir</div>
    <span class="gl tiny" style="top:119px">Glass<br><b style="font-size:5.4px">$9</b></span>
    <span class="bt tiny" style="top:119px">Bottle<br>$34<br>$36</span>

    <div class="wine" style="top:139.8px"><span class="cat">WHITES + ROSE</span>Domaine des Pins Le Vieux Rose</div>
    <div class="wine" style="top:155.1px">Clos d'Aubrac Chardonnay</div>
    <span class="gl tiny" style="top:144px">Glass<br>$8<br>$9</span>
    <span class="bt tiny" style="top:144px">Bottle<br>$32<br>$36</span>
    <div class="box" style="top:163.5px;height:27px"></div>
    <div class="wine" style="top:164px">Henri Dumas Sauvignon Blanc</div>
    <div class="wine" style="top:172.9px">Estate Riesling</div>
    <div class="wine" style="top:181.7px">Villa Serena Pinot Grigio</div>
    <span class="gl tiny" style="top:173px">Glass<br><b style="font-size:5.4px">$8</b></span>
    <span class="bt tiny" style="top:173px">Bottle<br><b style="font-size:5.4px">$32</b></span>

    <div class="wine" style="top:193.4px"><span class="cat">BUBBLES</span></div>
    <div class="wine" style="top:202.2px">Maison Ferrand-Roy Cremant de Bourgogne<br>Brut (NV)</div>
    <div class="wine" style="top:220px">Belle Rive Cremant de Loire Brut Rose</div>
    <div class="wine" style="top:228.3px">Paul Marchand Blanc de Blanc</div>
    <span class="gl tiny" style="top:201px">Glass<br>$12</span><span class="bt tiny" style="top:201px">Bottle<br>$48</span>
    <span class="gl tiny" style="top:215px">Glass<br>$14</span><span class="bt tiny" style="top:215px">Bottle<br>$56</span>
    <span class="gl tiny" style="top:228px">Glass<br>$9</span><span class="bt tiny" style="top:228px">Bottle<br>$36</span>

    <div class="wine" style="top:240.9px"><span class="cat">COCKTAILS</span><span class="cat">Mimosa</span><span class="ind">champagne, orange juice or cranberry</span><br>juice<span class="cat">Kir Royale</span><span class="ind">champagne, black currant liqueur</span></div>
    <span class="gl tiny" style="top:252px">Glass<br>$9</span><span class="bt tiny" style="top:252px">Bottle<br>$18</span>
    <span class="gl tiny" style="top:267px">Glass<br>$10</span>
    <div class="box" style="top:280px;height:37px"></div>
    <div class="wine" style="top:281.4px"><span class="cat">Peach Bellini</span><span class="ind">champagne, peach puree</span><span class="cat">Apple Cider-Mimosa</span><span class="ind">champagne, apple cider, caramel rim,</span><br>with brown sugar</div>
    <span class="gl tiny" style="top:290px">Glass<br>$9</span>
  </div>

  <div class="panel panel-3">
    <div class="panel-texture" role="img" aria-label="Faint line pattern of pastries and leaves"></div>
    <div class="blk" style="top:5.5px"><span class="n">Blood Orange or Pineapple Spritz</span><span class="d"><span class="ind">house blend vodka, sweet</span><br>vermouth, sugar cube, sparkling water with your<br>choice of flavored puree.</span></div>
    <div class="blk" style="top:34.5px"><span class="n">Bloody Mary</span><span class="d"><span class="ind">house blend vodka, fat &amp; juicy</span><br>bloody mary mix, celery</span></div>
    <div class="blk" style="top:54.5px"><span class="n">Espresso Martini</span><span class="d"><span class="ind">espresso shot, chocolate martini,</span><br>chocolate syrup</span></div>
    <div class="blk" style="top:74.5px"><span class="n">Chocolate Coffee Bomb</span><span class="d"><span class="ind">coffee, chocolate martini, whipped cream</span></span></div>
    <span class="p" style="top:6px;font-size:5px">Glass<br>$9</span>
    <span class="p" style="top:35px;font-size:5px">Glass<br>$9</span>
    <span class="p" style="top:53.5px;font-size:5px">Glass<br>$9</span>
    <span class="p" style="top:72.5px;font-size:5px">Glass<br>$9</span>
    <div class="blk" style="top:89.5px"><span class="n">COFFEES</span></div>
    <div class="blk" style="top:96.3px"><span class="d">Café Lumière coffee</span></div>
    <div class="blk" style="top:105.2px"><span class="d">Café Lumière espresso &amp; Americano</span></div>
    <div class="blk" style="top:114px"><span class="d">Cappuccino &amp; Latte</span></div>
    <div class="blk" style="top:122.9px"><span class="d">Café Mocha &amp; Café White Mocha</span></div>
    <div class="blk" style="top:131.8px"><span class="d">Chai Latte,Dirty Chai Latte, Truffle Latte<br>Napoleon Latte</span></div>
    <div class="blk" style="top:147.1px"><span class="d">Barraquito</span></div>
    <div class="blk" style="top:156px"><span class="d">White Chocolate Pumpkin Spice Latte</span></div>
    <div class="blk" style="top:164.8px"><span class="d">(seasonal)</span></div>
    <div class="blk" style="top:173.2px"><span class="d">Hot Cinnamon Vanilla Cider</span></div>
    <div class="blk" style="top:182px"><span class="d">Hot Cocoa</span></div>
    <span class="p" style="top:93px">$3</span>
    <span class="p" style="top:102.8px">$3.50</span>
    <span class="p" style="top:112.2px">$4</span>
    <span class="p" style="top:121.5px">$4.50</span>
    <span class="p" style="top:129.4px">$6</span>
    <span class="p" style="top:146.2px">$4.7</span>
    <span class="p" style="top:154.6px">$6</span>
    <span class="p" style="top:171.3px">$3</span>
    <span class="p" style="top:181.1px">$4</span>
    <div class="box" style="top:190px;height:28px"></div>
    <div class="blk" style="top:191.5px"><span class="d">FLAVORS: Vanilla, Salted Caramel,<br>Hazelnut, Chocolate, White Chocolate,<br>Lavender<br>MILK ALTERNATIVES: Almond, Oat</span></div>
    <span class="p" style="top:198.5px">$.50</span>
    <div class="blk" style="top:221px"><span class="d">Extra Shot</span></div>
    <span class="p" style="top:220px">$.51</span>
    <div class="blk" style="top:230.5px"><span class="n">BEVERAGES</span><span class="d">CANS SODA: Cola, Diet Cola, Lemon-Lime, Zero Cola<br>Pure Press &nbsp;&nbsp;&nbsp;assorted flavors<br>Fonte Chiara &nbsp;Blood Orange flavor<br>Belmont's &nbsp;&nbsp;&nbsp;assorted flavors</span><span class="n">Source Claire</span><span class="d">Val Doré &nbsp;&nbsp;&nbsp;assorted flavors<br>Island Spring water<br>Iced Tea</span></div>
    <span class="p" style="top:237px">$2.50</span>
    <span class="p" style="top:243.6px">$4.25</span>
    <span class="p" style="top:250.2px">$3.50</span>
    <span class="p" style="top:256.8px">Lg $9</span>
    <span class="p" style="top:256.8px;right:32px">Sm $9</span>
    <span class="p" style="top:263.4px">$2.50</span>
    <span class="p" style="top:270px">$7</span>
    <span class="p" style="top:276.6px">$3.50</span>
    <span class="p" style="top:283.2px">$2.50</span>
    <div class="box" style="top:289.5px;height:14px"></div>
    <div class="blk" style="top:290.5px"><span class="d">Meadow Peach Tea<br>Sunbrook &nbsp;&nbsp;&nbsp;&nbsp;&nbsp;&nbsp;&nbsp;&nbsp;assorted flavors<br>Juice: Cranberry, Orange<br>Milk, Chocolate Milk</span></div>
    <span class="p" style="top:293.5px">$3.50</span>
    <span class="p" style="top:304.2px">$3</span>
    <span class="p" style="top:310.8px">$2.50</span>
  </div>
</section>

</body>
</html>
```